a simple functional website for an up and coming service industry business

hi ,i also require in store promotional items like business cards, flyers, Facebook page t-shirts for workers and want all these to have the same look and feel.i need my website to catch the eye .the idea i have in my head is something that will sell the service ,the website is a tool to get people to inquire , book or pay for an assembly service.we assemble flatpack furniture , outdoor furniture,playgrounds etc ,basically anything that comes with instructions,our biggest customer at the moment is vormbo who we assemble nationally.i am looking for a website to be bright modern and simple to use the current website is www.pelmarbuildcrew.com which is dull with to many pages . i have already had a new logo designed by sketch harbor and it is lime green and sky blue in colour, a webiste i like is taskly q4 although it has lots of flash and my budget probably wouldn't allow that at the moment.

Target Market(s)

customer will be visiting the website to find out about the service we provide , then hopefully making contact,either booking a job or asking for a quote, i like the idea of the phone, email icons on the home screen

Industry/Entity Type

Industry

Requirements
Must have
• a contact icon: when you click on it the page with the name ,email address ,phone number, address pops up

a phone icon : when you click on it the 1300 number pops up
Nice to have
• my current website is with pagr and it is www.pelmarbuildcrew.com

a website i really like the design of is taskly q4 and vormbo

would like some pictures of modern furniture ,bbq's ,gym equipment ,playground equiptment
Should not have
• the career page or price page my current website .i don't want it on there anymore

```html
<!DOCTYPE html>
<html lang="en">
<head>
<meta charset="utf-8">
<title>Pelmar Assembly</title>
<link rel="stylesheet" href="https://fonts.googleapis.com/css2?family=Montserrat:wght@400;600&family=Open+Sans:wght@300;400;600;700&display=swap">
<style>
:root{
  --lime:#8dc63f;
  --lime-dark:#7ab32e;
  --sky:#1b8fd2;
  --ink:#333;
  --grey:#666;
  --muted:#999;
  --charcoal:#3a3a3a;
  --band:#3d3d3d;
  --white:#fff;
  --rule:#e4e4e4;
}
*{box-sizing:border-box;margin:0;padding:0}
html,body{width:708px;height:1200px;overflow:hidden;background:var(--white)}
body{position:relative;font-family:"Open Sans",Arial,sans-serif;color:var(--ink)}

/* bands */
.band-shapes{position:absolute;left:0;top:0;pointer-events:none}

/* header */
.site-header{position:absolute;left:95px;top:0;width:518px;height:60px;background:linear-gradient(#fff,#f2f2f2)}
.brand{position:absolute;left:14px;top:12px;display:flex;align-items:center;gap:8px}
.brand-square{width:30px;height:30px;background:var(--lime)}
.brand-name{font-family:"Open Sans",sans-serif;font-weight:700;color:var(--lime);font-size:19px;line-height:17px;letter-spacing:.5px}
.main-nav{position:absolute;left:208px;top:22px;display:flex}
.main-nav a{display:block;text-decoration:none;text-align:center;padding:0 9px;border-left:1px solid #cfd8e0;font-size:9.5px;color:var(--sky);line-height:12px}
.main-nav a:first-child{border-left:0}
.main-nav a span{display:block;font-size:7.5px;color:var(--grey)}
.main-nav a.book{color:var(--lime)}
.header-phone{position:absolute;left:116px;top:64px;display:flex;align-items:center;gap:6px;font-size:17px;line-height:22px;color:#222}
.licence{position:absolute;right:95px;top:64px;font-size:9px;color:#ddd;letter-spacing:.2px}

/* hero */
.hero{position:absolute;left:0;top:80px;width:708px;height:266px;background:linear-gradient(180deg,#e9ecef 0%,#f4f4f4 45%,#c9c4c0 100%)}
.hero-caption{position:absolute;left:387px;top:168px;width:226px;height:47px;background:var(--lime);color:var(--white);text-align:center;padding-top:6px}
.hero-caption h2{font-size:19px;font-weight:700;line-height:20px}
.hero-caption p{font-size:11px;color:#2f3b1d}
.hero-arrow{position:absolute;top:222px;width:30px;height:29px;background:#222;display:flex;align-items:center;justify-content:center}

/* services */
.section-title{position:absolute;left:0;width:708px;text-align:center;font-weight:600}
.services-title{top:363px;font-size:15px;color:var(--lime)}
.services-lead{top:383px;font-size:10px;color:var(--grey);font-weight:400}
.rule{position:absolute;left:130px;width:448px;height:1px;background:linear-gradient(90deg,transparent,var(--rule),transparent)}
.fitout-title{top:414px;font-size:15px;color:var(--sky)}
.service-card{position:absolute;width:260px;height:75px}
.service-card .thumb{position:absolute;left:0;top:0;width:111px;height:73px}
.service-card .body{position:absolute;left:121px;top:-2px;width:138px}
.service-card h3{font-size:11px;font-weight:400;color:#222;line-height:14px}
.service-card p{font-size:7px;line-height:8.2px;color:var(--grey);margin-top:2px}
.service-card a{font-size:7px;font-weight:700;color:var(--lime);text-decoration:none;display:block;margin-top:3px}
.more-link{top:644px;font-size:10px;color:var(--sky)}

/* contact band */
.contact-band{position:absolute;left:0;top:668px;width:708px;height:237px;background:linear-gradient(90deg,#5a3f33 0%,#7a5848 35%,#4a352c 60%,#6b4b3c 85%,#3c2a22 100%)}
.contact-form{position:absolute;left:95px;top:688px;width:218px}
.contact-form h2{font-family:"Montserrat",sans-serif;font-weight:600;font-size:14px;color:var(--white);line-height:16px}
.contact-form .note{font-size:6.5px;color:var(--white);line-height:8px;font-weight:600}
.field{display:block;width:218px;height:20px;background:var(--white);margin-top:4px;font-size:6px;color:#777;padding:6px 10px;font-family:inherit}
.contact-form .first{margin-top:8px}
.field.message{height:70px}
.send{display:block;width:218px;height:24px;background:var(--charcoal);color:var(--white);font-family:"Montserrat",sans-serif;font-size:11px;text-align:center;line-height:24px;margin-top:3px}
.services-panel{position:absolute;left:348px;top:688px;width:270px;color:var(--white)}
.services-panel h2{font-family:"Montserrat",sans-serif;font-weight:600;font-size:14px}
.services-panel .lead{font-size:10px;line-height:12px;margin-top:10px}
.svc-col{position:absolute;top:76px}
.svc-col h3{font-family:"Montserrat",sans-serif;font-size:9px;font-weight:600;margin-bottom:8px}
.svc-col ul{list-style:none}
.svc-col li{font-size:8.5px;line-height:16.3px;padding-left:16px;position:relative}
.svc-col li::before{content:"";position:absolute;left:0;top:5px;width:7px;height:7px;border-radius:50%;background:var(--white)}

/* benefits */
.help-title{top:920px;font-size:15px;color:#444;font-weight:300}
.benefit{position:absolute;width:150px}
.benefit svg{position:absolute;left:0;top:0}
.benefit h3{margin-left:17px;font-size:9.5px;font-weight:400;color:var(--sky);line-height:13px}
.benefit p{margin-left:17px;font-size:6.5px;line-height:8.3px;color:#444}
.quote-title{top:1083px;font-size:14px;color:var(--sky);font-weight:700}
.quote-sub{top:1100px;font-size:8.5px;color:#444;font-weight:400}

/* footer */
.footer-links{position:absolute;left:95px;top:1157px;font-size:6px;color:var(--white);white-space:nowrap}
.footer-links span{margin:0 3px;opacity:.8}
.footer-brand{position:absolute;left:286px;top:1135px;display:flex;align-items:center;gap:7px}
.footer-brand .brand-square{width:32px;height:32px}
.footer-brand .brand-name{font-size:18px;line-height:16px}
.footer-phone{position:absolute;left:491px;top:1126px;font-size:15px;color:#444;font-weight:300;display:flex;align-items:center;gap:5px}
.follow{position:absolute;left:467px;top:1156px;font-size:9px;color:var(--white);letter-spacing:.3px}
.social{position:absolute;top:1152px;width:20px;height:20px;border-radius:50%;background:var(--white)}
.copyright{position:absolute;left:0;top:1180px;width:708px;text-align:center;font-size:6.5px;color:#ccc}
</style>
</head>
<body>

<section class="hero" role="img" aria-label="Bright living room with a white sofa, cushions and a glass coffee table">
  <div class="hero-caption"><h2>DOMESTIC FIT OUTS</h2><p>Domestic Fit Outs Indoor Furniture</p></div>
  <div class="hero-arrow" style="left:552px"><svg width="10" height="14" viewBox="0 0 10 14"><path d="M8 1L2 7l6 6" stroke="#fff" stroke-width="2" fill="none"/></svg></div>
  <div class="hero-arrow" style="left:584px"><svg width="10" height="14" viewBox="0 0 10 14"><path d="M2 1l6 6-6 6" stroke="#fff" stroke-width="2" fill="none"/></svg></div>
</section>

<svg class="band-shapes" width="708" height="100" viewBox="0 0 708 100" aria-hidden="true">
  <rect x="280" y="60" width="428" height="20" fill="var(--band)"/>
  <polygon points="0,36 95,36 95,60 302,60 282,92 0,92" fill="var(--lime)"/>
</svg>

<header class="site-header">
  <div class="brand"><div class="brand-square"></div><div class="brand-name">PELMAR<br>ASSEMBLY</div></div>
  <nav class="main-nav">
    <a href="#">ABOUT US<span>Who we are?</span></a>
    <a href="#">SERVICES<span>What we do?</span></a>
    <a href="#">CONTACT US<span>Get in touch</span></a>
    <a href="#" class="book">BOOK &amp; SERVICES<span>&nbsp;</span></a>
  </nav>
</header>

<div class="header-phone">
  <svg width="18" height="18" viewBox="0 0 24 24"><path d="M6.6 10.8a15 15 0 0 0 6.6 6.6l2.2-2.2a1 1 0 0 1 1-.25 11.4 11.4 0 0 0 3.6.57 1 1 0 0 1 1 1V20a1 1 0 0 1-1 1A17 17 0 0 1 3 4a1 1 0 0 1 1-1h3.5a1 1 0 0 1 1 1c0 1.25.2 2.45.57 3.57a1 1 0 0 1-.25 1z" fill="#222"/></svg>
  1300-555-018
</div>
<div class="licence">QBSA LICENCE NUMBER:4410927</div>

<h2 class="section-title services-title">OUR SERVICES INCLUDE</h2>
<p class="section-title services-lead">We install DIY flat packed indoor and outdoor living, across South East Queensland for the major retailers.</p>
<div class="rule" style="top:407px"></div>
<h2 class="section-title fitout-title">DOMESTIC FIT OUT</h2>

<article class="service-card" style="left:95px;top:452px">
  <div class="thumb" role="img" aria-label="Modern bedroom furniture" style="background:linear-gradient(135deg,#3a2418,#8a5a3a 60%,#d9c4a8)"></div>
  <div class="body"><h3>Indoor furniture</h3><p>Lorem ipsum dolor sit amet, consectetuer adipiscing elit, sed diam nonummy nibh euismod tincidunt ut laoreet dolore magna aliquam erat volutpat.it, sed diam nonummy nibh euismod tincidunt ut laoreet dolore magna.</p><a href="#">Learn More &gt;&gt;</a></div>
</article>
<article class="service-card" style="left:359px;top:452px">
  <div class="thumb" role="img" aria-label="Outdoor wicker lounge set" style="background:linear-gradient(135deg,#8fb27a,#c9b89a 55%,#7a6a58)"></div>
  <div class="body" style="left:123px"><h3>Outdoor Furniture</h3><p>Lorem ipsum dolor sit amet, consectetuer adipiscing elit, sed diam nonummy nibh euismod tincidunt ut laoreet dolore magna aliquam erat volutpat.it, sed diam nonummy nibh euismod tincidunt ut laoreet dolore magna.</p><a href="#">Learn More &gt;&gt;</a></div>
</article>
<article class="service-card" style="left:95px;top:546px">
  <div class="thumb" role="img" aria-label="Colourful playground equipment" style="background:linear-gradient(180deg,#dfe8ef,#c46a3a 55%,#a08a60)"></div>
  <div class="body"><h3>Playgrounds</h3><p>Lorem ipsum dolor sit amet, consectetuer adipiscing elit, sed diam nonummy nibh euismod tincidunt ut laoreet dolore magna aliquam erat volutpat.it, sed diam nonummy nibh euismod tincidunt ut laoreet dolore magna.</p><a href="#">Learn More &gt;&gt;</a></div>
</article>
<article class="service-card" style="left:359px;top:546px">
  <div class="thumb" role="img" aria-label="Gym with rows of blue weight machines" style="background:linear-gradient(180deg,#6c7580,#2d4f8e 60%,#9aa0a6)"></div>
  <div class="body" style="left:123px"><h3>Gyms</h3><p>Lorem ipsum dolor sit amet, consectetuer adipiscing elit, sed diam nonummy nibh euismod tincidunt ut laoreet dolore magna aliquam erat volutpat.it, sed diam nonummy nibh euismod tincidunt ut laoreet dolore magna.</p><a href="#">Learn More &gt;&gt;</a></div>
</article>
<div class="rule" style="top:633px"></div>
<p class="section-title more-link">View More Our Services</p>

<section class="contact-band" role="img" aria-label="Blurred warm-toned interior backdrop"></section>
<form class="contact-form">
  <h2>FILL OUR CONTACT FORM</h2>
  <p class="note">to discuss your requirements and one of our prompt installers will contact you within 24 business hours.</p>
  <div class="field first">NAME</div>
  <div class="field">EMAIL</div>
  <div class="field">PHONE</div>
  <div class="field message">MESSAGE</div>
  <div class="send">SEND</div>
</form>
<div class="services-panel">
  <h2>OUR SERVICES</h2>
  <p class="lead">We install DIY flat packed indoor and outdoor living, across South East Queensland for the major retailers.</p>
  <div class="svc-col" style="left:0;width:130px">
    <h3>COMMERCIAL FIT OUT</h3>
    <ul><li>Office</li><li>Interior Designer fit out</li><li>Hotel</li><li>Display home</li><li>Kitchen - assembly and installation</li></ul>
  </div>
  <div class="svc-col" style="left:166px">
    <h3>DOMESTIC FIT OUT</h3>
    <ul><li>Indoor furniture</li><li>Outdoor Furniture</li><li>Sheds</li><li>Playgrounds</li><li>BBQ's</li><li>Gyms</li></ul>
  </div>
</div>

<h2 class="section-title help-title">How Can We Help Your Assembly Service</h2>

<div class="benefit" style="left:104px;top:961px"><svg width="13" height="13" viewBox="0 0 13 13"><circle cx="6.5" cy="6.5" r="6.5" fill="var(--lime)"/><path d="M3.5 6.7l2 2 4-4.2" stroke="#fff" stroke-width="1.6" fill="none"/></svg><h3>Reliability</h3><p>Lorem ipsum dolor sit amet, consectetuer adipiscing elit, sed diam nonummy nibh euismod tincidunt ut laoreet</p></div>
<div class="benefit" style="left:269px;top:961px"><svg width="13" height="13" viewBox="0 0 13 13"><circle cx="6.5" cy="6.5" r="6.5" fill="var(--lime)"/><path d="M3.5 6.7l2 2 4-4.2" stroke="#fff" stroke-width="1.6" fill="none"/></svg><h3>Efficiency</h3><p>Lorem ipsum dolor sit amet, consectetuer adipiscing elit, sed diam nonummy nibh euismod tincidunt ut laoreet</p></div>
<div class="benefit" style="left:437px;top:961px"><svg width="13" height="13" viewBox="0 0 13 13"><circle cx="6.5" cy="6.5" r="6.5" fill="var(--lime)"/><path d="M3.5 6.7l2 2 4-4.2" stroke="#fff" stroke-width="1.6" fill="none"/></svg><h3>Flexibility</h3><p>Lorem ipsum dolor sit amet, consectetuer adipiscing elit, sed diam nonummy nibh euismod tincidunt ut laoreet</p></div>
<div class="benefit" style="left:104px;top:1010px"><svg width="13" height="13" viewBox="0 0 13 13"><circle cx="6.5" cy="6.5" r="6.5" fill="var(--lime)"/><path d="M3.5 6.7l2 2 4-4.2" stroke="#fff" stroke-width="1.6" fill="none"/></svg><h3>Excellent Communication</h3><p>Lorem ipsum dolor sit amet, consectetuer adipiscing elit, sed diam nonummy nibh euismod tincidunt ut laoreet</p></div>
<div class="benefit" style="left:269px;top:1010px"><svg width="13" height="13" viewBox="0 0 13 13"><circle cx="6.5" cy="6.5" r="6.5" fill="var(--lime)"/><path d="M3.5 6.7l2 2 4-4.2" stroke="#fff" stroke-width="1.6" fill="none"/></svg><h3>Personal Shopper/Delivery</h3><p>Lorem ipsum dolor sit amet, consectetuer adipiscing elit, sed diam nonummy nibh euismod tincidunt ut laoreet</p></div>
<div class="benefit" style="left:437px;top:1010px"><svg width="13" height="13" viewBox="0 0 13 13"><circle cx="6.5" cy="6.5" r="6.5" fill="var(--lime)"/><path d="M3.5 6.7l2 2 4-4.2" stroke="#fff" stroke-width="1.6" fill="none"/></svg><h3>Handyman Services</h3><p>Lorem ipsum dolor sit amet, consectetuer adipiscing elit, sed diam nonummy nibh euismod tincidunt ut laoreet</p></div>

<div class="rule" style="top:1074px"></div>
<h2 class="section-title quote-title">Get a fixed Price Quote</h2>
<p class="section-title quote-sub">It Only Takes Few Minutes</p>

<footer>
  <svg class="band-shapes" style="top:1100px" width="708" height="100" viewBox="0 1100 708 100" aria-hidden="true">
    <rect x="0" y="1148" width="708" height="24" fill="var(--lime)"/>
    <polygon points="264,1172 282,1122 430,1122 448,1172" fill="var(--white)"/>
    <rect x="0" y="1172" width="708" height="28" fill="var(--band)"/>
  </svg>
  <nav class="footer-links">About Us<span>|</span>Jobs<span>|</span>Privacy<span>|</span>Terms of Use<span>|</span>Sitemap</nav>
  <div class="footer-brand"><div class="brand-square"></div><div class="brand-name">PELMAR<br>ASSEMBLY</div></div>
  <div class="footer-phone">1300-555-018
    <svg width="16" height="16" viewBox="0 0 24 24"><path d="M6.6 10.8a15 15 0 0 0 6.6 6.6l2.2-2.2a1 1 0 0 1 1-.25 11.4 11.4 0 0 0 3.6.57 1 1 0 0 1 1 1V20a1 1 0 0 1-1 1A17 17 0 0 1 3 4a1 1 0 0 1 1-1h3.5a1 1 0 0 1 1 1c0 1.25.2 2.45.57 3.57a1 1 0 0 1-.25 1z" fill="#444"/></svg>
  </div>
  <div class="follow">FOLLOW US ON</div>
  <span class="social" style="left:543px"></span>
  <span class="social" style="left:568px"></span>
  <span class="social" style="left:593px"></span>
  <p class="copyright">© 2013 PELMAR INSTALLATIONS PTY LTD</p>
</footer>

</body>
</html>
```